website conversion to Wordpress with an updated look and feel

Brim Tarn Works Limited is a company and an online presence, which promotes and sells a branded fuel additive product named “Pelvix”.

The existing website is at www.brimtarnworks.co.uk

The site consists of static but attractive pages, a contact form, and most importantly a shopping page which is driven externally using shopvarn.com. Therefore e-commerce coding is NOT required as this task is performed by shopvarn via a plugin.

The website is 4 years old and we intend to revamp the graphics and the image of the company and the website to give it a modern “Windows 10” look!

Less text and less cluttering, Cleaner and easier navigations, bigger and clearer fonts. Simple message to put across to visitors/potential customers. Be creative.

The site needs to be simplified - the detail can/should still be there... But it can be placed deeper down or hidden by the use of dropdowns, callouts, etc.

A couple of good example styles we like are

https://www.gullmoth.com/
http://www.9brassling.com/en/#/welcome
https://www.slatetorro.com/

Some specific areas of attention.

homepage - This needs to really reflect the new look-and feel of the website. In addition the product we sell can be used in a number of applications - currently navigation to these different applications is through the moving banner. This needs to be changed. The major areas for access should be

Heating Oil
Vehicles
Marine
Generators

Technical requirements what we want:-
Wordpress (self hosted ) - currently Joomla based
Use of webfonts to improve typographic appearances
Shopvarn integration using plugin
Flockpage/Chirpline integration
Responsive design (Mobile friendly)
Search Engine friendly and some SEO optimisation
Google Analytics / Bing webmaster tracking

Target Market(s)

Owners of Tolv branded range cookers and similar - our product fixes a fuel problem specific to these devices.

Also bulk fuel users looking to save money on their fuel costs - product improves fuel efficiency and reduces maintenance.

Industry/Entity Type

E-Commerce

Font styles to use
Sans Serif

Requirements
Must have
• Wordpress design
• Responsive design
• Simple "clean" look and feel
• Use of stock graphics
• a review of all current pages
Nice to have
• Social media integration - blog
• A forum to discuss the product and problems people experience with fuel

```html
<!DOCTYPE html>
<html lang="en">
<head>
<meta charset="utf-8">
<title>Brim Tarn Works – Home</title>
<link rel="stylesheet" href="https://fonts.googleapis.com/css2?family=Roboto:wght@400;500;700&family=Open+Sans:wght@400;600&family=Oswald:wght@600&display=swap">
<style>
:root{
  --page:#e6e8ef;
  --white:#ffffff;
  --ink:#1e1e1e;
  --green:#6aa531;
  --orange:#f15a22;
  --teal:#1fae8a;
  --yellow:#f9ab1b;
  --blue:#2a7ec2;
  --red:#e0322b;
  --purple:#9b4fc7;
  --footer:#272727;
  --footer-text:#e8e8e8;
  --star:#f0a21b;
  --video:#dfe8cf;
}
*{box-sizing:border-box;margin:0;padding:0}
html,body{width:713px;height:1200px;overflow:hidden}
body{position:relative;background:var(--page);font-family:"Open Sans",Arial,sans-serif;color:var(--ink)}
.abs{position:absolute}
.top-bar{left:0;top:0;width:713px;height:30px;background:#f7f7f9;border-bottom:1px solid #dcdde3}
.call-us{left:58px;top:8px;font:500 11px "Roboto",sans-serif}
.call-us span{font-weight:400;font-size:10px;margin-left:4px}
.call-us i{display:inline-block;width:8px;height:8px;background:var(--green);border-radius:2px;margin-left:4px;vertical-align:-1px}
.social-dots{right:58px;top:7px;display:flex;gap:4px}
.social-dots b{width:17px;height:17px;border:1px solid #cfd0d6;border-radius:50%;background:#fff}
.brand{left:58px;top:45px;width:173px;height:60px;background:var(--white);border:1px solid #dadbe1;padding:10px 0 0 10px}
.brand-name{display:flex;align-items:center;gap:5px;font:500 15px "Roboto",sans-serif;color:#333}
.brand-name i{width:14px;height:14px;border-radius:50%;background:var(--green)}
.brand-tag{font-size:6.5px;color:#555;margin:3px 0 0 19px;line-height:10px}
.main-nav{left:241px;top:45px;width:413px;height:60px;background:var(--white);border:1px solid #dadbe1;display:flex}
.nav-item{flex:1 1 auto;display:flex;flex-direction:column;align-items:center;padding-top:12px;font:400 8.5px "Roboto",sans-serif;border-right:1px solid #eee}
.nav-item:last-child{border-right:none}
.nav-icon{height:18px;display:flex;align-items:center;justify-content:center;margin-bottom:9px}
.hero{left:59px;top:122px;width:595px;height:289px;background:linear-gradient(100deg,#2f4a6a 0%,#6f8fb0 25%,#b9d3ea 50%,#9ec07c 75%,#4f7a3a 100%);overflow:hidden}
.hero-title{left:25px;top:176px;font:600 44px "Oswald",sans-serif;color:var(--white);text-shadow:2px 2px 3px rgba(0,0,0,.55);letter-spacing:.5px}
.hero-arrow{top:235px;width:28px;height:27px;border:1px solid rgba(255,255,255,.8);display:flex;align-items:center;justify-content:center}
.tile{top:430px;width:137px;height:164px;color:var(--white);text-align:center}
.tile-icon{width:60px;height:60px;border-radius:50%;background:var(--white);margin:13px auto 0;display:flex;align-items:center;justify-content:center}
.tile h3{font:400 12.5px "Roboto",sans-serif;margin-top:17px;letter-spacing:.3px}
.tile p{font-size:7.2px;line-height:12px;margin:4px 10px 0;opacity:.95}
.tile .chev{margin-top:4px}
.welcome{left:59px;top:614px;width:595px;height:218px;background:var(--white);border:1px solid #dadbe1}
.welcome h2{position:absolute;left:15px;top:20px;font:500 15px "Roboto",sans-serif}
.welcome h2 em{font-style:normal;color:var(--green)}
.welcome p{position:absolute;left:15px;width:305px;font-size:6.5px;line-height:12.2px;color:#333}
.btn-videos{left:16px;top:170px;width:116px;height:24px;background:var(--green);color:var(--white);font:400 9px "Roboto",sans-serif;display:flex;align-items:center;justify-content:center}
.video{left:339px;top:23px;width:241px;height:171px;background:#f2f2f2;border:1px solid #cfd6c4;overflow:hidden}
.video-still{left:0;top:0;width:239px;height:152px;background:linear-gradient(180deg,#e4ecd6,var(--video))}
.player{left:0;bottom:0;width:239px;height:18px;background:#f2f2f2;border-top:1px solid #ddd}
.testimonials{left:59px;top:854px;width:595px;height:158px;background:var(--white);border:1px solid #dadbe1}
.testimonials h2{position:absolute;left:15px;top:18px;font:400 11.5px "Roboto",sans-serif}
.testimonials hr{position:absolute;left:15px;top:44px;width:565px;border:none;border-top:1px solid #e3e3e3}
.avatar{width:70px;height:70px;border-radius:50%;border:2px solid #e4e4e4;background:linear-gradient(180deg,#d9dee6,#8896ad)}
.quote{width:165px;font-size:7px;line-height:11.3px;color:#444}
.quote b{font:700 10px Georgia,serif;color:#666;margin-right:6px;vertical-align:-1px}
.stars{color:var(--star);font-size:7px;letter-spacing:1px;margin-top:3px}
.name{color:var(--green);font:400 8.5px "Roboto",sans-serif;margin-top:5px}
.footer{left:0;top:1034px;width:713px;height:128px;background:var(--footer);color:var(--footer-text)}
.footer h4{font:400 9.5px "Roboto",sans-serif;letter-spacing:.3px;margin-bottom:10px}
.footer p,.footer li{font-size:6.6px;line-height:12px}
.tweet{display:flex;gap:9px;margin-bottom:6px}
.tweet i{flex:none;width:10px;height:10px;background:var(--white);border-radius:2px;margin-top:2px}
.signup{display:flex;margin-top:14px}
.signup span{width:110px;height:23px;border:1px solid #444;font-size:6.5px;color:#888;padding:7px}
.signup b{width:47px;height:23px;background:#e9a92d;color:var(--white);font:400 9px "Roboto",sans-serif;display:flex;align-items:center;justify-content:center}
.footer ul{list-style:none}
.footer li{display:flex;align-items:center;gap:8px;margin-bottom:5px}
.footer li i{width:6px;height:6px;background:var(--white);border-radius:50%}
.legal{left:0;top:1162px;width:713px;height:38px;background:var(--green);color:var(--white);font-size:6px;display:flex;align-items:center;justify-content:center;letter-spacing:.2px}
</style>
</head>
<body>

<header>
  <div class="abs top-bar">
    <div class="abs call-us">Call Us :<i></i><span>0800 915</span></div>
    <div class="abs social-dots"><b></b><b></b><b></b></div>
  </div>

  <div class="abs brand">
    <div class="brand-name"><i></i>Brim Tarn Works</div>
    <div class="brand-tag">Economy · Efficiency · Environment<br>The Fuel Additive Specialists</div>
  </div>

  <nav class="abs main-nav">
    <div class="nav-item" style="color:var(--blue)">
      <span class="nav-icon"><svg width="16" height="15" viewBox="0 0 16 15"><path d="M8 1 1 7h2v7h4V10h2v4h4V7h2z" fill="var(--blue)"/></svg></span>HOME</div>
    <div class="nav-item" style="color:var(--red)">
      <span class="nav-icon"><svg width="20" height="16" viewBox="0 0 20 16"><circle cx="7" cy="9" r="5" fill="none" stroke="var(--red)" stroke-width="3" stroke-dasharray="2 1.2"/><circle cx="15" cy="5" r="3.5" fill="none" stroke="var(--red)" stroke-width="2.4" stroke-dasharray="1.6 1"/></svg></span>HOW IT WORKS</div>
    <div class="nav-item" style="color:var(--teal)">
      <span class="nav-icon"><svg width="18" height="14" viewBox="0 0 18 14"><path d="M2 12C2 4 9 1 17 1c0 8-5 12-12 11z" fill="var(--green)"/><path d="M3 12 11 5" stroke="#fff" stroke-width="1"/></svg></span>ENVIRONMENT</div>
    <div class="nav-item" style="color:var(--yellow)">
      <span class="nav-icon"><svg width="16" height="16" viewBox="0 0 16 16"><circle cx="8" cy="8" r="6.5" fill="none" stroke="#f08c1b" stroke-width="1.6"/><path d="M1.5 8h13M8 1.5v13M3.5 3.5q4 4.5 0 9M12.5 3.5q-4 4.5 0 9" fill="none" stroke="#f08c1b" stroke-width="1.2"/></svg></span>APPLICATIONS</div>
    <div class="nav-item" style="color:var(--purple)">
      <span class="nav-icon"><svg width="18" height="16" viewBox="0 0 18 16"><rect x="5" y="1" width="7" height="6" fill="var(--purple)"/><rect x="1" y="8" width="7" height="7" fill="var(--purple)"/><rect x="9" y="8" width="7" height="7" fill="var(--purple)"/></svg></span>STORE</div>
    <div class="nav-item" style="color:var(--ink)">
      <span class="nav-icon"><svg width="18" height="14" viewBox="0 0 18 14"><rect x="1" y="1" width="16" height="12" rx="1.5" fill="none" stroke="#444" stroke-width="1.4"/><path d="M1 2l8 6 8-6" fill="none" stroke="#444" stroke-width="1.4"/></svg></span>CONTACT</div>
  </nav>
</header>

<main>
  <section class="abs hero" role="img" aria-label="Photo of a hand refuelling a car with a red fuel nozzle, trees and sky behind">
    <div class="abs hero-title">Premium Fuel</div>
    <div class="abs hero-arrow" style="left:28px"><svg width="8" height="12" viewBox="0 0 8 12"><path d="M6 1 1 6l5 5" fill="none" stroke="#fff" stroke-width="1.3"/></svg></div>
    <div class="abs hero-arrow" style="left:59px"><svg width="8" height="12" viewBox="0 0 8 12"><path d="M2 1l5 5-5 5" fill="none" stroke="#fff" stroke-width="1.3"/></svg></div>
  </section>

  <section class="applications">
    <article class="abs tile" style="left:59px;background:var(--green)">
      <div class="tile-icon"><svg width="28" height="30" viewBox="0 0 28 30"><path d="M9 1q-2 3 0 5t0 5M14 1q-2 3 0 5t0 5M19 1q-2 3 0 5t0 5" fill="none" stroke="var(--green)" stroke-width="1.6"/><path d="M4 13h20v3a10 10 0 0 1-20 0z" fill="var(--green)"/><path d="M6 29h16l-2-6H8z" fill="var(--green)"/></svg></div>
      <h3>HEATING OIL</h3>
      <p>Proin gravida nibh vel velit auctor aliquet. Aenean sollicitudin, lorem quis bibendum auctor.</p>
      <svg class="chev" width="10" height="10" viewBox="0 0 10 10"><path d="M1 1l4 4 4-4M1 5l4 4 4-4" fill="none" stroke="#fff" stroke-width="1.5"/></svg>
    </article>
    <article class="abs tile" style="left:211px;background:var(--orange)">
      <div class="tile-icon"><svg width="30" height="24" viewBox="0 0 30 24"><path d="M7 2h16l4 9v10h-5v-3H8v3H3V11z" fill="var(--orange)"/><path d="M9 5h12l2 6H7z" fill="#fff"/><circle cx="8" cy="14" r="2" fill="#fff"/><circle cx="22" cy="14" r="2" fill="#fff"/></svg></div>
      <h3>VEHICLES</h3>
      <p>Proin gravida nibh vel velit auctor aliquet. Aenean sollicitudin, lorem quis bibendum auctor.</p>
      <svg class="chev" width="10" height="10" viewBox="0 0 10 10"><path d="M1 1l4 4 4-4M1 5l4 4 4-4" fill="none" stroke="#fff" stroke-width="1.5"/></svg>
    </article>
    <article class="abs tile" style="left:364px;background:var(--teal)">
      <div class="tile-icon"><svg width="26" height="30" viewBox="0 0 26 30"><circle cx="13" cy="4" r="2.6" fill="none" stroke="var(--teal)" stroke-width="2"/><path d="M13 7v20M7 11h12M2 17q1 10 11 10t11-10" fill="none" stroke="var(--teal)" stroke-width="2.6"/></svg></div>
      <h3>MARINE</h3>
      <p>Proin gravida nibh vel velit auctor aliquet. Aenean sollicitudin, lorem quis bibendum auctor.</p>
      <svg class="chev" width="10" height="10" viewBox="0 0 10 10"><path d="M1 1l4 4 4-4M1 5l4 4 4-4" fill="none" stroke="#fff" stroke-width="1.5"/></svg>
    </article>
    <article class="abs tile" style="left:518px;background:var(--yellow)">
      <div class="tile-icon"><svg width="30" height="28" viewBox="0 0 30 28"><rect x="3" y="7" width="24" height="16" rx="1" fill="var(--yellow)"/><rect x="10" y="2" width="12" height="9" fill="#fff" stroke="var(--yellow)" stroke-width="1.5"/><path d="M17 3l-3 4h3l-2 3" fill="none" stroke="var(--yellow)" stroke-width="1.3"/><rect x="6" y="13" width="6" height="6" fill="#fff"/><path d="M5 23v3M25 23v3" stroke="var(--yellow)" stroke-width="2"/></svg></div>
      <h3>GENERATORS</h3>
      <p>Proin gravida nibh vel velit auctor aliquet. Aenean sollicitudin, lorem quis bibendum auctor.</p>
      <svg class="chev" width="10" height="10" viewBox="0 0 10 10"><path d="M1 1l4 4 4-4M1 5l4 4 4-4" fill="none" stroke="#fff" stroke-width="1.5"/></svg>
    </article>
  </section>

  <section class="abs welcome">
    <h2>WELCOME TO <em>BRIM TARN WORKS</em></h2>
    <p style="top:43px">With the cost of fuel constantly increasing – imagine the benefits to you if you could improve vehicle MPG by even a few percent. Whether you are a multinational road haulier running a fleet of vehicles or if you only drive to the shops once a week PELVIX can save you money on your fuel bill and reduce the impact to the environment.</p>
    <p style="top:104px">PELVIX is a 100% organic fuel treatment which reduces the harmful effects of impurities in modern fuels and improves combustion. It is a fantastic product with huge benefits for the both the domestic user and for industry. Already well-established in shipping (PELVIX treated 30 million tonnes of fuel last year) it is now available in the UK, offering improved engine efficiency, reduced pollutants and better fuel economy.</p>
    <div class="abs btn-videos">WATCH MORE VIDEOS</div>
    <div class="abs video">
      <div class="abs video-still" role="img" aria-label="Video still showing the product title card on a pale green background"></div>
      <svg class="abs" style="left:105px;top:61px" width="30" height="30" viewBox="0 0 30 30"><circle cx="15" cy="15" r="14" fill="rgba(255,255,255,.7)"/><path d="M12 9l9 6-9 6z" fill="#9aa58a"/></svg>
      <div class="abs player">
        <svg width="239" height="18" viewBox="0 0 239 18"><path d="M9 6l5 3-5 3z" fill="#222"/><text x="28" y="11.5" font-size="5.5" font-family="Open Sans,sans-serif" fill="#333">10:00/05:03</text><rect x="69" y="8" width="120" height="2" fill="#333"/><rect x="69" y="8" width="56" height="2" fill="var(--red)"/><path d="M199 7h2l3-2v8l-3-2h-2z" fill="#222"/><rect x="210" y="8" width="22" height="2" fill="var(--red)"/></svg>
      </div>
    </div>
  </section>

  <section class="abs testimonials">
    <h2>TESTIMONIALS</h2>
    <hr>
    <div class="abs avatar" style="left:16px;top:68px" role="img" aria-label="Portrait photo of a customer in a suit"></div>
    <div class="abs" style="left:101px;top:71px">
      <div class="quote"><b>“</b>Nulla sollicitudin tincidunt dui et egestas. Phasellus non sem tum, ullamcorper vitae, accumsan dui. Duis dignissim condi lorem. Maecenas facilisis ipsum sed porttitor rutrum.</div>
      <div class="stars">★★★☆☆</div>
      <div class="name">TOM HADLEY</div>
    </div>
    <div class="abs avatar" style="left:330px;top:68px" role="img" aria-label="Portrait photo of a customer in a suit"></div>
    <div class="abs" style="left:415px;top:71px">
      <div class="quote"><b>“</b>Nulla sollicitudin tincidunt dui et egestas. Phasellus non sem tum, ullamcorper vitae, accumsan dui. Duis dignissim condi lorem. Maecenas facilisis ipsum sed porttitor rutrum.</div>
      <div class="stars">★★★☆☆</div>
      <div class="name">TOM HADLEY</div>
    </div>
  </section>
</main>

<footer>
  <div class="abs footer">
    <div class="abs" style="left:57px;top:15px;width:150px">
      <h4>ABOUT US</h4>
      <p>Lorem ipsum dolor sit amet, consectetur adipisicing elit, sed do eiusmod tempor incididunt ut labore et dolore magna aliqua. Ut enim ad minim veniam, quis nostrud exercitation ullamco laboris nisi ut aliquip</p>
    </div>
    <div class="abs" style="left:233px;top:15px;width:140px">
      <h4>LATEST TWEET`S</h4>
      <div class="tweet"><i></i><p>Good morning .... wherever you are today! All of us at ...See more here http://t.co/K4rp2Ld9Qw</p></div>
      <div class="tweet"><i></i><p>Good morning .... wherever you are today! All of us at ...See more here http://t.co/K4rp2Ld9Qw</p></div>
    </div>
    <div class="abs" style="left:396px;top:19px;width:165px">
      <h4>NEWSLETTER</h4>
      <p>Excepteur sint occaecat cupidatat non proident, sunt in culpa qui officia deserunt mollit anim</p>
      <div class="signup"><span>Enter your email address</span><b>Sign Up</b></div>
    </div>
    <div class="abs" style="left:592px;top:15px">
      <h4>SOCIAL MEDIA</h4>
      <ul>
        <li><i></i>Flockpage</li>
        <li><i></i>Chirpline</li>
        <li><i></i>Orbit Plus</li>
        <li><i></i>ReelTube</li>
      </ul>
    </div>
  </div>
  <div class="abs legal">© 2015 BRIM TARN WORKS - ALL RIGHTS RESERVED</div>
</footer>

</body>
</html>
```